Anzeigengestaltung für Unternehmensberatung für Pflegedienste
Zielgruppe
Wir sind eine Unternehmensberatung für Pflegedienste. Es soll eine Werbeanzeige erstellt werden, mit welcher schlecht laufende Pflegedienste, die gerade in einer Krise stecken angesprochen werden,
Der slogan soll einfach klingen : Pflege neu gedaxht: wirtschaftlich, nachhaltig, zukunftssicher
Anzeige in 3 Formaten
1. Format 55.3 mm x 118 mm
2. Format 1/ halbe Seite Quer 176 x 118 mm un
3. Format d 1 x A4 _Seite
Der Name der Firma Keltor GmbH info at keltor.de Tel 0381 72958143 aus Rostock Berlin und bundesweit tätig
Aufgabenstellung
Kreativ und elegant

```html
<!DOCTYPE html>
<html lang="de">
<head>
<meta charset="utf-8">
<title>Keltor GmbH – Anzeige</title>
<link rel="stylesheet" href="https://fonts.googleapis.com/css2?family=Noto+Sans:wght@400;500;700&display=swap">
<style>
  :root {
    --page-bg: #dde3e6;
    --card-bg: #f1ede4;
    --navy: #1c3a5c;
    --ink: #1e1e1e;
    --ink-soft: #2b2b2b;
  }
  html, body {
    margin: 0;
    padding: 0;
    width: 1200px;
    height: 900px;
    overflow: hidden;
    background: var(--page-bg);
    font-family: "Noto Sans", Arial, sans-serif;
  }
  .ad {
    position: absolute;
    left: 360px;
    top: 75px;
    width: 480px;
    height: 750px;
    background: var(--card-bg);
    box-sizing: border-box;
  }
  .brand {
    position: absolute;
    top: 58px;
    right: 38px;
    margin: 0;
    font-size: 44px;
    font-weight: 500;
    letter-spacing: 3px;
    color: var(--navy);
    line-height: 1;
  }
  .headline {
    position: absolute;
    left: 38px;
    top: 160px;
    width: 410px;
    margin: 0;
    font-size: 37px;
    font-weight: 700;
    line-height: 42px;
    color: var(--ink);
  }
  .intro {
    position: absolute;
    left: 38px;
    top: 395px;
    width: 400px;
    margin: 0;
    font-size: 20px;
    line-height: 29px;
    color: var(--ink-soft);
  }
  .contact {
    position: absolute;
    left: 38px;
    top: 662px;
    margin: 0;
    font-size: 19px;
    line-height: 32px;
    color: var(--ink-soft);
  }
</style>
</head>
<body>
  <article class="ad">
    <p class="brand">KELTOR</p>
    <h1 class="headline">Pflege neu gedacht: wirtschaftlich, nachhaltig, zukunftssicher</h1>
    <p class="intro">Stagniert Ihr Pflegedienst in der Krise? Wir analysieren Strukturen, senken Kosten und sichern Ihre Zukunft mit klaren Konzepten für nachhaltigen Erfolg.</p>
    <p class="contact">info@keltor.de&nbsp; | &nbsp;Tel 0381 72958143<br>Rostock, Berlin &amp; Nationwide</p>
  </article>
</body>
</html>
```